Business Card Design Project

I have attached the logo and the colour pallete for the branding for the company.

Creative designs for business cards are needed.

The Company is modern corporate.

Industry/Entity Type

Business

```html
<!DOCTYPE html>
<html lang="en">
<head>
<meta charset="utf-8">
<title>knowhub business card</title>
<link rel="stylesheet" href="https://fonts.googleapis.com/css2?family=Lato:wght@400;700&display=swap">
<style>
  :root {
    --page: #e9e6e1;
    --card: #000000;
    --glow: #8a8a8a;
    --glow-soft: #b5b5b5;
    --ink: #ffffff;
    --ink-soft: #e6e6e6;
    --shadow: rgba(0, 0, 0, 0.28);
  }
  * { box-sizing: border-box; margin: 0; padding: 0; }
  html, body {
    width: 1200px;
    height: 646px;
    overflow: hidden;
    background: var(--page);
    font-family: "Lato", sans-serif;
    color: var(--ink);
  }
  .canvas {
    position: relative;
    width: 1200px;
    height: 646px;
  }
  .card {
    position: absolute;
    top: 168px;
    width: 540px;
    height: 309px;
    background: var(--card);
    box-shadow: 0 10px 28px var(--shadow);
    overflow: hidden;
  }
  .card--front {
    left: 40px;
    background:
      radial-gradient(ellipse 240px 170px at 52% 22%, var(--glow) 0%, rgba(60,60,60,0.7) 40%, rgba(0,0,0,0) 100%),
      var(--card);
  }
  .card--back {
    left: 620px;
    background:
      radial-gradient(ellipse 260px 190px at 18% 100%, var(--glow-soft) 0%, rgba(70,70,70,0.6) 45%, rgba(0,0,0,0) 100%),
      var(--card);
  }
  .tagline {
    position: absolute;
    left: 28px;
    top: 88px;
    width: 170px;
    font-size: 13px;
    font-weight: 700;
    line-height: 1.3;
    color: var(--ink-soft);
  }
  .brand-name {
    position: absolute;
    right: 26px;
    top: 118px;
    font-size: 34px;
    font-weight: 700;
    letter-spacing: -0.5px;
    color: var(--ink);
  }
  .person {
    position: absolute;
    right: 32px;
    top: 40px;
    text-align: right;
    font-size: 22px;
    font-weight: 400;
    line-height: 1.2;
  }
  .contacts {
    position: absolute;
    left: 26px;
    bottom: 38px;
    list-style: none;
  }
  .contacts li {
    display: flex;
    align-items: center;
    gap: 9px;
    height: 22px;
    font-size: 13px;
    font-weight: 700;
  }
  .contacts svg {
    width: 17px;
    height: 17px;
    flex: none;
  }
</style>
</head>
<body>
<main class="canvas">

  <section class="card card--front" aria-label="Business card front">
    <p class="tagline">Your first online help and resource centre for all everyday questions</p>
    <p class="brand-name">knowhub</p>
  </section>

  <section class="card card--back" aria-label="Business card back">
    <div class="person">
      <p class="person__name">John Doe</p>
      <p class="person__role">CEO</p>
    </div>

    <ul class="contacts">
      <li>
        <svg viewBox="0 0 20 20" aria-hidden="true"><circle cx="10" cy="10" r="9" fill="none" stroke="#fff" stroke-width="1.4"/><path d="M6.5 5.5c.6-.6 1.3-.4 1.6.2l.7 1.4c.2.5 0 .9-.4 1.2l-.5.4c.5 1.2 1.4 2.1 2.6 2.6l.4-.5c.3-.4.8-.5 1.2-.3l1.4.7c.6.3.8 1 .2 1.6-1 1-2.6 1.1-4.3-.3-1.5-1.1-2.6-2.6-3.1-3.9-.5-1.3-.3-2.4.2-3.1z" fill="#fff"/></svg>
        <span>0100 200 300</span>
      </li>
      <li>
        <svg viewBox="0 0 20 20" aria-hidden="true"><circle cx="10" cy="10" r="9" fill="none" stroke="#fff" stroke-width="1.4"/><rect x="7" y="4.5" width="6" height="11" rx="1" fill="none" stroke="#fff" stroke-width="1.3"/><circle cx="10" cy="13.5" r="0.8" fill="#fff"/></svg>
        <span>0400 500 600</span>
      </li>
      <li>
        <svg viewBox="0 0 20 20" aria-hidden="true"><circle cx="10" cy="10" r="9" fill="none" stroke="#fff" stroke-width="1.4"/><circle cx="10" cy="10" r="2.2" fill="none" stroke="#fff" stroke-width="1.3"/><path d="M12.2 8v2.8c0 1 1.6 1.2 1.8-.3.3-2.4-1.6-4.5-4-4.5a4 4 0 1 0 2 7.5" fill="none" stroke="#fff" stroke-width="1.3"/></svg>
        <span>office@knowhub.com</span>
      </li>
      <li>
        <svg viewBox="0 0 20 20" aria-hidden="true"><circle cx="10" cy="10" r="8" fill="none" stroke="#fff" stroke-width="1.4"/><ellipse cx="10" cy="10" rx="3.4" ry="8" fill="none" stroke="#fff" stroke-width="1.1"/><path d="M2 10h16M3.2 6h13.6M3.2 14h13.6" stroke="#fff" stroke-width="1.1"/></svg>
        <span>www.knowhub</span>
      </li>
      <li>
        <svg viewBox="0 0 20 20" aria-hidden="true"><circle cx="10" cy="10" r="7" fill="#fff"/></svg>
        <span>/knowhub</span>
      </li>
      <li>
        <svg viewBox="0 0 20 20" aria-hidden="true"><circle cx="10" cy="10" r="7" fill="#fff"/></svg>
        <span>@knowhub</span>
      </li>
    </ul>
  </section>

</main>
</body>
</html>
```